Geschäftspapiere für Lasergravuren
Zielgruppe
Lasergravuren z.B. auf Glas, Holz, Filz, Papier, Acryl, eloxierten Aluminium zu Dekorationszwecken,
Ausschneiden von Elementen z.B. aus Holz, Filz, Papier, Acryl usw. zu Dekorationszwecken mit dem Lasergravierer.
Anfertigung verschiedener Dekorationsartikel,
Zielgruppe: Frauen (mit Familien) aller Altersgruppen, die Freude am Dekorieren und Verschenken haben
Aufgabenstellung
Das vorhandene Logo soll mit eingebunden werden

```html
<!DOCTYPE html>
<html lang="de">
<head>
<meta charset="utf-8">
<title>Lunaro – Briefbogen</title>
<link rel="stylesheet" href="https://fonts.googleapis.com/css2?family=Open+Sans:wght@400;600&family=Arimo:wght@400&display=swap">
<style>
  :root {
    --gold: #b38840;
    --grey: #707070;
    --text: #5a5a5a;
    --paper: #ffffff;
  }
  * { box-sizing: border-box; margin: 0; padding: 0; }
  html, body { width: 866px; height: 1200px; overflow: hidden; background: var(--paper); }
  .letterhead {
    position: relative;
    width: 866px;
    height: 1200px;
    background: var(--paper);
    font-family: "Open Sans", Arial, sans-serif;
    color: var(--text);
  }
  .side-band {
    position: absolute; left: 0; top: 0;
    width: 26px; height: 100%;
    background: var(--gold);
  }
  .side-band::before, .side-band::after {
    content: ""; position: absolute; top: 0; width: 1.5px; height: 100%;
    background: var(--paper);
  }
  .side-band::before { left: 5px; }
  .side-band::after { left: 10px; }
  .fold-mark {
    position: absolute; left: 0; width: 30px; height: 1px;
    background: var(--gold);
  }
  .fold-mark.upper { top: 410px; }
  .fold-mark.lower { top: 802px; }
  .brand {
    position: absolute; top: 40px; left: 0; width: 100%;
    display: flex; flex-direction: column; align-items: center; gap: 10px;
  }
  .brand-circle {
    width: 66px; height: 66px; border-radius: 50%;
    border: 1.5px solid var(--gold);
  }
  .brand-name {
    font-size: 56px; font-weight: 400; line-height: 1;
    color: var(--grey); letter-spacing: 1px;
  }
  .sender-line {
    position: absolute; top: 210px; left: 87px;
    font-family: "Arimo", Arial, sans-serif;
    font-size: 9.5px; color: var(--text);
    padding-bottom: 1px;
    border-bottom: 1px solid #9a9a9a;
  }
  .sender-line .sep { color: var(--gold); margin: 0 2px; }
  .footer-bar {
    position: absolute; top: 1085px; left: 95px; right: 0;
    height: 21px; background: var(--grey);
  }
  .footer-ornament {
    position: absolute; top: 1053px; left: 6px;
    width: 92px; height: 84px;
    background: radial-gradient(ellipse at 60% 50%, var(--grey) 0 32%, rgba(179,136,64,0.45) 55%, rgba(255,255,255,0) 72%);
  }
  .footer-contact {
    position: absolute; top: 1118px; left: 205px;
    display: flex; gap: 42px;
    font-size: 14px; line-height: 19px; color: var(--text);
  }
  .contact-row { display: flex; align-items: center; gap: 6px; }
  .contact-row svg { width: 12px; height: 12px; fill: var(--gold); flex: none; }
</style>
</head>
<body>
<main class="letterhead">
  <div class="side-band"></div>
  <div class="fold-mark upper"></div>
  <div class="fold-mark lower"></div>

  <header class="brand">
    <div class="brand-circle"></div>
    <div class="brand-name">Lunaro</div>
  </header>

  <p class="sender-line">Ahornweg 12 <span class="sep">|</span> 30453 Musterstadt</p>

  <div class="footer-bar"></div>
  <div class="footer-ornament" role="img" aria-label="Ornament: Laserspitze mit Strahlen"></div>

  <footer class="footer-contact">
    <address class="contact-block" style="font-style:normal">
      <div>Birkenallee 8</div>
      <div>31135 Beispielstadt</div>
    </address>
    <div class="contact-block">
      <div class="contact-row">
        <svg viewBox="0 0 12 12"><path d="M2.5 1l2 2.2-1 1.3c.8 1.6 2 2.8 3.6 3.6l1.3-1 2.2 2-1.2 1.6C5 10.3 1.7 7 .9 2.2z"/></svg>
        <span>0511 / 123 45 67</span>
      </div>
      <div class="contact-row">
        <svg viewBox="0 0 12 12"><path d="M3 1h6v3H3zM1 4.5h10V9H9v2H3V9H1zM4 7.5v2.5h4V7.5z"/></svg>
        <span>0511 / 123 45 68</span>
      </div>
    </div>
    <div class="contact-block">
      <div class="contact-row">
        <svg viewBox="0 0 12 12"><path d="M6 .5a5.5 5.5 0 100 11 5.5 5.5 0 000-11zm0 1.2c.6.6 1.1 1.9 1.3 3.3H4.7C4.9 3.6 5.4 2.3 6 1.7zM1.8 6.2h1.8c0 1.3.3 2.5.8 3.4a4.3 4.3 0 01-2.6-3.4zm0-1.2a4.3 4.3 0 012.6-3.4c-.5.9-.8 2.1-.8 3.4zm4.2 5.3c-.6-.6-1.1-1.8-1.3-3.1h2.6c-.2 1.3-.7 2.5-1.3 3.1zm1.6-.7c.5-.9.8-2.1.8-3.4h1.8a4.3 4.3 0 01-2.6 3.4zm.8-4.6c0-1.3-.3-2.5-.8-3.4A4.3 4.3 0 0110.2 5z"/></svg>
        <span>www.lunaro-deko.de</span>
      </div>
      <div class="contact-row">
        <svg viewBox="0 0 12 12"><path d="M6 1l5 3.5V11H1V4.5zM2.2 5l3.8 2.7L9.8 5 6 2.4z"/></svg>
        <span>post@lunaro-deko.de</span>
      </div>
    </div>
  </footer>
</main>
</body>
</html>
```